Business Card Design Project - bel soravin group

dear Sirs

we need business card design for our group ( BEL Soravin Group ) , i have got the Logo design of our group from pixel harbor in previous , so all need details relating to our group i think available with you, as well as the the chosen logo design

we hope to provide us with business card logo that to be appropaite and satisfactory to us .

thanks

note : logo design of our group is attached .
Updates

Reason: please extend the deadline of my project for additional 15 days because i didn't received appropriate design for our gruop yet . kindly beaware that i have received 77 design till now , supossed to send me 200-250 design at least . thanks

Target Market(s)

contents
-

name : Korvan EL Mistrani

position : Operation Manager

Industry/Entity Type

Business

Requirements
Must have

• person name

group logo
Nice to have
• logo color matching with back background

```html
<!DOCTYPE html>
<html lang="en">
<head>
<meta charset="utf-8">
<title>BEL Soravin Group – Business Card</title>
<link rel="stylesheet" href="https://fonts.googleapis.com/css2?family=Arvo:ital,wght@0,400;1,400&display=swap">
<style>
  :root {
    --bg: #171717;
    --bg-deep: #121212;
    --teal: #2e7b86;
    --teal-line: #3a8e99;
    --brand-blue: #34449a;
    --rule: rgba(120, 170, 180, 0.55);
  }
  html, body {
    margin: 0;
    padding: 0;
    width: 1023px;
    height: 1200px;
    overflow: hidden;
    background: var(--bg);
  }
  .canvas {
    position: relative;
    width: 1023px;
    height: 1200px;
    font-family: "Arvo", Georgia, serif;
  }
  .card-side {
    position: absolute;
    left: 0;
    width: 1023px;
    height: 600px;
    background: var(--bg);
    overflow: hidden;
  }
  .card-front {
    top: 0;
    background: linear-gradient(to bottom, var(--bg) 0%, var(--bg) 82%, var(--bg-deep) 100%);
  }
  .card-back { top: 600px; }

  .rule-horizontal {
    position: absolute;
    height: 1px;
    background: linear-gradient(to right, transparent, var(--rule) 20%, var(--rule) 80%, transparent);
  }
  .front-rule-top { top: 169px; left: 150px; width: 752px; background: linear-gradient(to right, transparent, var(--teal-line) 25%, var(--teal-line) 75%, transparent); }
  .front-rule-bottom { top: 420px; left: 130px; width: 772px; }

  .brand-name {
    position: absolute;
    top: 244px;
    left: 0;
    width: 1023px;
    text-align: center;
    margin: 0;
    font-size: 62px;
    font-weight: 400;
    line-height: 1;
    letter-spacing: 2px;
    color: var(--brand-blue);
  }

  .back-divider {
    position: absolute;
    left: 539px;
    top: 50px;
    width: 2px;
    height: 506px;
    background: linear-gradient(to bottom, transparent, rgba(150, 190, 200, 0.5) 15%, rgba(150, 190, 200, 0.5) 85%, transparent);
  }
  .contact-rule {
    position: absolute;
    height: 2px;
    background: linear-gradient(to right, transparent, var(--teal-line) 30%, var(--teal-line) 85%, transparent);
  }
  .contact-rule-1 { top: 309px; left: 169px; width: 433px; }
  .contact-rule-2 { top: 362px; left: 141px; width: 461px; }
  .contact-rule-3 { top: 413px; left: 113px; width: 489px; }
  .contact-rule-4 { top: 464px; left: 94px; width: 508px; }

  .person {
    position: absolute;
    left: 604px;
    top: 120px;
    width: 325px;
    text-align: right;
    color: var(--teal);
  }
  .person-name {
    margin: 0;
    font-size: 39px;
    font-weight: 400;
    line-height: 1.1;
    white-space: nowrap;
  }
  .person-title {
    margin: -4px 0 0;
    font-size: 18px;
    font-style: italic;
    line-height: 1.1;
  }

  .contact-list {
    position: absolute;
    left: 602px;
    top: 262px;
    margin: 0;
    padding: 0;
    list-style: none;
    color: var(--teal);
    font-size: 40px;
    line-height: 51.5px;
    letter-spacing: 1px;
  }
  .contact-list li:nth-child(n+4) { padding-left: 5px; }
</style>
</head>
<body>
<div class="canvas">
  <section class="card-side card-front" aria-label="Card front">
    <div class="rule-horizontal front-rule-top"></div>
    <h1 class="brand-name">BEL SORAVIN GROUP</h1>
    <div class="rule-horizontal front-rule-bottom"></div>
  </section>

  <section class="card-side card-back" aria-label="Card back">
    <div class="back-divider"></div>
    <div class="contact-rule contact-rule-1"></div>
    <div class="contact-rule contact-rule-2"></div>
    <div class="contact-rule contact-rule-3"></div>
    <div class="contact-rule contact-rule-4"></div>

    <div class="person">
      <p class="person-name">Korvan EL Mistrani</p>
      <p class="person-title">Operation Manager</p>
    </div>

    <ul class="contact-list">
      <li>Fax</li>
      <li>Mobile</li>
      <li>Website</li>
      <li>E-mail</li>
      <li>Telephone</li>
    </ul>
  </section>
</div>
</body>
</html>
```